BrookvaleLogic Website Design

To design a website for BrookvaleLogic, a software development company. The website should reflect the branding of our company, which is Smart, Beautiful, and Sophisticated. The existing website is www.brookvalelogic-example.com.sg

```html
<!DOCTYPE html>
<html lang="en">
<head>
<meta charset="utf-8">
<title>BrookvaleLogic</title>
<link href="https://fonts.googleapis.com/css2?family=Teko:wght@500&family=Roboto:wght@400;500&family=Source+Sans+3:wght@400&display=swap" rel="stylesheet">
<style>
:root{
  --navy:#0b3a5c;
  --navy-deep:#082a44;
  --blue:#1a7fc0;
  --blue-bright:#1f8fd6;
  --header-bg:#e6e6e6;
  --nav-top:#f2f3f3;
  --nav-bottom:#d6d8d9;
  --nav-line:#b9bcbe;
  --text-grey:#888;
  --slide-text:#4a4a4a;
  --box-line:#d8d8d8;
  --mission-bg:#f2f2f2;
}
*{margin:0;padding:0;box-sizing:border-box}
html,body{width:1200px;height:938px;overflow:hidden;background:#fff;font-family:'Roboto',sans-serif}
.page{position:relative;width:1200px;height:938px;overflow:hidden}
.top-bar{position:absolute;left:0;top:0;width:1200px;height:10px;background:linear-gradient(90deg,var(--navy-deep),#1c5f86 60%,#2a7199)}
.header{position:absolute;left:0;top:10px;width:1200px;height:271px;background:var(--header-bg)}
.brand{position:absolute;left:386px;top:60px;width:430px;height:96px}
.brand-mark{position:absolute;left:0;top:0;width:94px;height:94px;border-radius:50%;background:var(--navy)}
.brand-name{position:absolute;left:108px;top:26px;font-family:'Roboto',sans-serif;font-weight:400;font-size:41px;color:var(--blue);letter-spacing:.5px;line-height:1}
.brand-tag{position:absolute;right:4px;top:74px;font-size:11.5px;color:#222;font-family:'Roboto',sans-serif}
.nav{position:absolute;left:132px;top:208px;width:936px;height:52px;background:linear-gradient(var(--nav-top),var(--nav-bottom));border:1px solid var(--nav-line);box-shadow:0 2px 4px rgba(0,0,0,.2);display:flex;padding-left:70px}
.nav a{display:flex;align-items:center;justify-content:center;height:100%;font-size:15px;color:#1f3a4e;text-decoration:none;border-right:1px solid var(--nav-line)}
.nav a.active{background:var(--navy);color:#fff;border-right:none}
.slider{position:absolute;left:132px;top:260px;width:936px;height:230px}
.slide-photo{position:absolute;inset:0;background:linear-gradient(110deg,#3a3a3a 0%,#8a8580 28%,#c9c2b8 34%,#e6ddd0 55%,#efe7da 100%)}
.slide-caption{position:absolute;right:53px;top:115px;text-align:right;font-family:'Roboto',sans-serif;font-weight:500;font-size:24px;line-height:30px;color:var(--slide-text)}
.arrow{position:absolute;top:84px}
.dots{position:absolute;left:437px;top:205px;display:flex;gap:17px}
.dots span{width:13px;height:13px;border-radius:50%;background:#8a8581}
.dots span.on{background:#111}
.section-title{position:absolute;left:0;width:1200px;text-align:center;font-family:'Teko',sans-serif;font-weight:500;font-size:44px;line-height:1;letter-spacing:.5px}
.products-title{top:535px;color:var(--blue)}
.services{position:absolute;left:133px;top:600px;width:935px;height:234px;border:1px solid var(--box-line);display:flex}
.service{flex:1;border-right:1px solid var(--box-line);position:relative}
.service:last-child{border-right:none}
.service-icon{position:absolute;top:42px;width:114px;height:114px;border-radius:50%;background:linear-gradient(var(--navy),var(--navy-deep));display:flex;align-items:center;justify-content:center}
.service-label{position:absolute;top:178px;left:0;right:0;text-align:center;font-family:'Source Sans 3',sans-serif;font-size:15px;color:var(--text-grey)}
.mission{position:absolute;left:0;top:868px;width:1200px;height:70px;background:var(--mission-bg)}
.mission-title{top:897px;color:var(--navy-deep)}
</style>
</head>
<body>
<div class="page">
  <div class="top-bar"></div>
  <header class="header">
    <div class="brand">
      <div class="brand-mark"></div>
      <div class="brand-name">BrookvaleLogic</div>
      <div class="brand-tag">A software development company</div>
    </div>
  </header>

  <nav class="nav">
    <a class="active" href="#" style="width:77px">HOME</a>
    <a href="#" style="width:215px">COMPANY PROFILE</a>
    <a href="#" style="width:221px">BOARD OF DIRECTORS</a>
    <a href="#" style="width:123px">ABOUT US</a>
    <a href="#" style="width:139px">CONTACT US</a>
  </nav>

  <section class="slider">
    <div class="slide-photo" role="img" aria-label="Photo of a tablet showing an e-book page lying on a light wooden desk"></div>
    <svg class="arrow" style="left:38px" width="30" height="44" viewBox="0 0 30 44"><path d="M24 4 8 22l16 18" fill="none" stroke="#222" stroke-width="6"/></svg>
    <svg class="arrow" style="left:898px" width="30" height="44" viewBox="0 0 30 44"><path d="M6 4l16 18L6 40" fill="none" stroke="#555" stroke-width="6"/></svg>
    <p class="slide-caption">We produce high interactive<br>digital media and software<br>for the mobile world</p>
    <div class="dots"><span class="on"></span><span></span><span></span></div>
  </section>

  <h2 class="section-title products-title">PRODUCTS AND SERVICES</h2>

  <section class="services">
    <div class="service">
      <div class="service-icon" style="left:60px">
        <svg width="44" height="56" viewBox="0 0 44 56"><path d="M6 3h22l13 13v34a3 3 0 0 1-3 3H6a3 3 0 0 1-3-3V6a3 3 0 0 1 3-3z" fill="none" stroke="#fff" stroke-width="4" stroke-linejoin="round"/><path d="M28 3v13h13" fill="none" stroke="#fff" stroke-width="4"/></svg>
      </div>
      <div class="service-label">Software Applications</div>
    </div>
    <div class="service">
      <div class="service-icon" style="left:60px">
        <svg width="56" height="62" viewBox="0 0 56 62"><rect x="3" y="3" width="34" height="52" rx="4" fill="none" stroke="#fff" stroke-width="4"/><path d="M10 18 16 10M10 26 20 12" stroke="#fff" stroke-width="2.5"/><circle cx="20" cy="49" r="2.5" fill="#fff"/><rect x="29" y="24" width="24" height="36" rx="3" fill="var(--navy)" stroke="#fff" stroke-width="4"/><path d="M35 36l5-6" stroke="#fff" stroke-width="2.5"/><circle cx="41" cy="54" r="2" fill="#fff"/></svg>
      </div>
      <div class="service-label">Mobile Applications</div>
    </div>
    <div class="service">
      <div class="service-icon" style="left:62px">
        <svg width="74" height="50" viewBox="0 0 74 50"><path d="M16 48a14 14 0 0 1-2-28A18 18 0 0 1 48 12a13 13 0 0 1 14 10 13 13 0 0 1-2 26z" fill="#fff"/><path d="M37 20 25 33h8v15h8V33h8z" fill="var(--navy)"/></svg>
      </div>
      <div class="service-label">Hosting</div>
    </div>
    <div class="service">
      <div class="service-icon" style="left:52px">
        <svg width="58" height="56" viewBox="0 0 58 56">
          <g transform="translate(20 34)"><g fill="#fff"><rect x="-4" y="-19" width="8" height="38" rx="1"/><rect x="-4" y="-19" width="8" height="38" rx="1" transform="rotate(45)"/><rect x="-4" y="-19" width="8" height="38" rx="1" transform="rotate(90)"/><rect x="-4" y="-19" width="8" height="38" rx="1" transform="rotate(135)"/><circle r="14"/></g><circle r="6" fill="var(--navy)"/></g>
          <g transform="translate(44 14)"><g fill="#fff"><rect x="-3" y="-13" width="6" height="26" rx="1"/><rect x="-3" y="-13" width="6" height="26" rx="1" transform="rotate(45)"/><rect x="-3" y="-13" width="6" height="26" rx="1" transform="rotate(90)"/><rect x="-3" y="-13" width="6" height="26" rx="1" transform="rotate(135)"/><circle r="9.5"/></g><circle r="4" fill="var(--navy)"/></g>
        </svg>
      </div>
      <div class="service-label">Maintenance Services</div>
    </div>
  </section>

  <section class="mission"></section>
  <h2 class="section-title mission-title">MISSION AND VISION</h2>
</div>
</body>
</html>
```